Design an Elegant Handbag Brand website

I need a webiste design are looking for ideas for a new theme, color scheme, etc. You come up with the general look and feel of the home page and our team will take it from there.
We're only looking for a one (1) page layout which should be fashionable and graphic intensive, but also include the standard homepage links (about us, see our collections, etc)

Target Market(s)

Our customers are fashionable women looking for an animal friendly and environmentally friendly handbag.

Industry/Entity Type

Business

Number of Pages Required

1 page

Font styles to use
Serif
Sans Serif

Requirements
Must have
• Feel free to modify it with different colors or tweaks as you see fit. We are open to all suggestions.
Nice to have

```html
<!DOCTYPE html>
<html lang="en">
<head>
<meta charset="utf-8">
<title>Handbags — Home</title>
<link rel="stylesheet" href="https://fonts.googleapis.com/css2?family=Bodoni+Moda:wght@400;500&family=Open+Sans:wght@400&family=Arimo:wght@400&display=swap">
<style>
  :root {
    --ink: #000000;
    --text: #222222;
    --nav-text: #444444;
    --notice-bg: #e1e1e1;
    --frame: #5f5b5b;
    --sale-bg: #f58f80;
    --navy: #0f1763;
    --white: #ffffff;
    --pay: #fcc42b;
    --footer-bg: #eff0f0;
    --bag-black: #1e1e1e;
    --bag-tan: #c4ab8c;
    --bag-brown: #4a3126;
    --bag-coral: #f2574f;
  }
  * { box-sizing: border-box; margin: 0; padding: 0; }
  html, body { width: 1051px; height: 1200px; overflow: hidden; background: var(--white); }
  body { position: relative; font-family: "Open Sans", sans-serif; color: var(--text); }
  .abs { position: absolute; }

  .notice { left: 0; top: 19px; width: 1051px; height: 59px; background: var(--notice-bg);
    display: flex; align-items: center; justify-content: center; font-size: 16px; color: var(--text); }

  .page-frame { left: 10px; top: 109px; width: 1030px; height: 995px; border: 6px solid var(--frame); }

  .rule { background: var(--ink); }
  .rule-top { left: 72px; top: 143px; width: 913px; height: 11px; }
  .rule-mid { left: 80px; top: 594px; width: 914px; height: 12px; }

  .tool-icons { left: 90px; top: 176px; }
  .cart { left: 912px; top: 172px; }

  .brand-title { left: 0; width: 1051px; top: 160px; text-align: center;
    font-family: "Bodoni Moda", serif; font-weight: 400; font-size: 72px; line-height: 1; color: var(--ink); }

  .category-nav { left: 110px; top: 257px; width: 840px; height: 40px; border: 1px solid var(--ink);
    display: flex; justify-content: space-between; align-items: center; padding: 0 14px 0 12px;
    font-size: 17px; color: var(--nav-text); }

  .arrow { top: 429px; }
  .arrow-prev { left: 54px; }
  .arrow-next { left: 946px; }

  .photo { display: block; }
  .bag-tote { left: 172px; top: 326px; width: 153px; height: 198px; background: linear-gradient(180deg, #2c2c2c, var(--bag-black)); border-radius: 6px 6px 10px 10px; }
  .bag-set { left: 674px; top: 342px; width: 226px; height: 204px; background: linear-gradient(160deg, #cdb597, var(--bag-tan)); border-radius: 10px; }

  .sale-panel { left: 374px; top: 310px; width: 277px; height: 266px; background: var(--sale-bg);
    text-align: center; color: var(--navy); font-family: "Bodoni Moda", serif; }
  .sale-panel .headline { position: absolute; left: 0; width: 100%; top: 75px; font-size: 60px; line-height: 50px; font-weight: 500; }
  .sale-panel .offer { position: absolute; left: 46px; top: 187px; width: 182px; height: 48px; background: var(--navy);
    color: var(--white); font-size: 36px; line-height: 48px; }

  .section-title { left: 0; width: 1051px; top: 638px; text-align: center; font-family: "Bodoni Moda", serif;
    font-size: 56px; line-height: 1; color: var(--ink); letter-spacing: 0.5px; }

  .shop-now { left: 379px; top: 717px; width: 331px; height: 78px; background: var(--ink); color: var(--white);
    font-family: "Arimo", sans-serif; font-size: 25px; display: flex; align-items: center; justify-content: center; }

  .bag-duffel { left: 74px; top: 862px; width: 230px; height: 170px; background: linear-gradient(180deg, #5a3c2e, var(--bag-brown)); border-radius: 30px 30px 8px 8px; }
  .bag-hobo { left: 626px; top: 818px; width: 114px; height: 245px; background: linear-gradient(180deg, #f46c64, var(--bag-coral)); border-radius: 40px 40px 50px 50px; }

  .product-info { width: 205px; font-family: "Bodoni Moda", serif; color: var(--ink); }
  .product-info .name { font-size: 11.5px; line-height: 12.5px; text-transform: uppercase; }
  .product-info .price { margin-top: 5px; font-size: 11.5px; letter-spacing: 0.6px; }
  .product-info .was { text-decoration: line-through; margin-right: 12px; }
  .info-a { left: 311px; top: 925px; }
  .info-b { left: 763px; top: 925px; }

  .btn-cart { height: 19px; width: 194px; border: 1px solid #555; border-radius: 4px; background: var(--white);
    font-family: "Arimo", sans-serif; font-size: 12px; display: flex; align-items: center; justify-content: center; color: var(--ink); }
  .btn-pay { height: 19px; width: 192px; border-radius: 4px; background: var(--pay);
    font-family: "Arimo", sans-serif; font-size: 12px; display: flex; align-items: center; justify-content: center; color: var(--navy); }
  .btn-pay small { font-size: 7px; margin-right: 3px; color: var(--ink); }
  .cart-a { left: 313px; top: 977px; }
  .pay-a { left: 315px; top: 1004px; }
  .cart-b { left: 766px; top: 977px; }
  .pay-b { left: 768px; top: 1004px; }

  .back-to-top { left: 90px; top: 1123px; width: 907px; height: 56px; background: var(--footer-bg);
    display: flex; align-items: center; justify-content: center; gap: 18px; font-family: "Arimo", sans-serif; font-size: 20px; color: var(--ink); }
</style>
</head>
<body>
  <div class="abs notice">We’re currently experiencing delays in shipping and returns.&nbsp; Thank you for your patience.</div>

  <div class="abs page-frame"></div>

  <div class="abs rule rule-top"></div>

  <svg class="abs tool-icons" width="46" height="22" viewBox="0 0 46 22" aria-label="Menu and search">
    <g stroke="#222" stroke-width="2" stroke-linecap="round">
      <line x1="1" y1="4" x2="20" y2="4"/><line x1="1" y1="10" x2="20" y2="10"/><line x1="1" y1="16" x2="20" y2="16"/>
    </g>
    <circle cx="31" cy="10" r="6.5" fill="none" stroke="#222" stroke-width="3"/>
    <line x1="36" y1="15" x2="42" y2="21" stroke="#222" stroke-width="3.5" stroke-linecap="round"/>
  </svg>

  <svg class="abs cart" width="56" height="28" viewBox="0 0 56 28" aria-label="Cart, 0 items">
    <circle cx="12" cy="13" r="12" fill="#222"/>
    <text x="12" y="18" text-anchor="middle" fill="#fff" font-family="Arimo, sans-serif" font-size="13" font-weight="700">0</text>
    <path d="M28 4 h5 l3 13 h14 l3 -10 h-19" fill="none" stroke="#222" stroke-width="3" stroke-linejoin="round"/>
    <circle cx="38" cy="23" r="2.3" fill="#222"/><circle cx="48" cy="23" r="2.3" fill="#222"/>
  </svg>

  <h1 class="abs brand-title">Handbags</h1>

  <nav class="abs category-nav">
    <span>Shoulder Bags</span><span>Totes</span><span>Hobo Bags</span><span>Wristlets</span><span>Satchels</span>
  </nav>

  <svg class="abs arrow arrow-prev" width="24" height="44" viewBox="0 0 24 44" aria-label="Previous">
    <polyline points="22,2 2,22 22,42" fill="none" stroke="#333" stroke-width="1.5"/>
  </svg>
  <svg class="abs arrow arrow-next" width="24" height="44" viewBox="0 0 24 44" aria-label="Next">
    <polyline points="2,2 22,22 2,42" fill="none" stroke="#333" stroke-width="1.5"/>
  </svg>

  <div class="abs photo bag-tote" role="img" aria-label="Black structured tote bag with long handles"></div>

  <div class="abs sale-panel">
    <div class="headline">SPRING<br>SALE</div>
    <div class="offer">20% Off</div>
  </div>

  <div class="abs photo bag-set" role="img" aria-label="Set of three taupe handbags with tassel and chain details"></div>

  <div class="abs rule rule-mid"></div>

  <h2 class="abs section-title">SHOP OUR LATEST RELEASES</h2>

  <div class="abs shop-now">SHOP NOW</div>

  <div class="abs photo bag-duffel" role="img" aria-label="Brown patterned barrel handbag with dark top handle"></div>
  <div class="abs product-info info-a">
    <div class="name">Rue Marceau Women's<br>Luxury Fashion PVC Handbag</div>
    <div class="price">$159.99</div>
  </div>
  <div class="abs btn-cart cart-a">Add to Cart</div>
  <div class="abs btn-pay pay-a"><small>Buy With</small>SwiftPay</div>

  <div class="abs photo bag-hobo" role="img" aria-label="Coral red slouchy hobo bag with shoulder strap"></div>
  <div class="abs product-info info-b">
    <div class="name">Harbor Hobo - Coral<br>Pebble</div>
    <div class="price"><span class="was">$159.99</span>$129.99</div>
  </div>
  <div class="abs btn-cart cart-b">Add to Cart</div>
  <div class="abs btn-pay pay-b"><small>Buy With</small>SwiftPay</div>

  <div class="abs back-to-top">
    <span>Back to Top</span>
    <svg width="18" height="9" viewBox="0 0 18 9" aria-hidden="true"><polygon points="0,9 9,0 18,9" fill="#000"/></svg>
  </div>
</body>
</html>
```